Business Card Design - Corporate

Create a sleek elegant business card layout while suggesting a color scheme. Convey cutting edge technology while maintaining a corporate feel that is easily readable.

Company designs and manufactures consumer electronic products for mass retail that are mainly app driven.

(vector logo and die-line provided)

Target Market(s)

Corporate level, tech industry.

Industry/Entity Type

Business

Contact Information for Business Card

Generic Info:

Name
Title
email
address
phone 1
phone 2
website (vantorelle.com) on back

Font styles to use
Sans Serif

Requirements
Must have
• At least 2 colors + white on one side.
Nice to have
• Solid suggestion on color for logo and overall design. Color flood on back of card.
Should not have
• background texture like... marble, stone, patterns or circuit boards

```html
<!DOCTYPE html>
<html lang="en">
<head>
<meta charset="UTF-8">
<title>Vantorelle Business Card</title>
<link rel="stylesheet" href="https://fonts.googleapis.com/css2?family=Open+Sans:wght@400;600;700&display=swap">
<style>
  :root {
    --stage: #1c2130;
    --card-white: #ffffff;
    --card-grey: #595959;
    --ink-dark: #2e3138;
    --ink-light: #ffffff;
    --accent: #1a86e0;
  }
  * { margin: 0; padding: 0; box-sizing: border-box; }
  html, body {
    width: 1200px; height: 900px; overflow: hidden;
    background: var(--stage);
    font-family: "Open Sans", sans-serif;
  }
  .stage {
    position: relative; width: 1200px; height: 900px;
  }
  .card {
    position: absolute;
    width: 500px; height: 290px;
    border-radius: 26px;
  }
  .card--front {
    left: 640px; top: 150px;
    background: var(--card-white);
    display: flex; align-items: center; justify-content: center;
  }
  .card--back {
    left: 60px; top: 460px;
    background: var(--card-grey);
    color: var(--ink-light);
  }
  .brand {
    display: flex; align-items: center; gap: 10px;
    font-weight: 400; letter-spacing: 6px; text-transform: uppercase;
  }
  .brand__dot {
    width: 14px; height: 14px; border-radius: 50%;
    background: var(--accent);
  }
  .card--front .brand { font-size: 34px; color: var(--ink-dark); }
  .card--back .brand {
    position: absolute; left: 150px; top: 40px;
    font-size: 34px; color: var(--ink-light);
  }
  .person {
    position: absolute; left: 150px; top: 98px;
  }
  .person__name { font-size: 22px; font-weight: 700; line-height: 1.1; }
  .person__title { font-size: 15px; color: var(--accent); line-height: 1.3; }
  .contact {
    position: absolute; left: 150px; top: 160px;
    list-style: none; font-size: 14px; line-height: 23px;
  }
  .contact__item { display: flex; align-items: center; gap: 9px; }
  .contact__icon { width: 13px; height: 13px; flex: none; }
</style>
</head>
<body>
<main class="stage">
  <section class="card card--front" aria-label="Card front">
    <div class="brand"><span class="brand__name">Vantorelle</span><span class="brand__dot"></span></div>
  </section>

  <section class="card card--back" aria-label="Card back">
    <div class="brand"><span class="brand__name">Vantorelle</span><span class="brand__dot"></span></div>
    <div class="person">
      <p class="person__name">Your Name</p>
      <p class="person__title">Designation</p>
    </div>
    <ul class="contact">
      <li class="contact__item">
        <svg class="contact__icon" viewBox="0 0 16 16"><rect x="1" y="3" width="14" height="10" fill="var(--accent)"/><path d="M1 3 L8 9 L15 3" fill="none" stroke="var(--card-grey)" stroke-width="1.5"/></svg>
        info@yourwebsite.nl
      </li>
      <li class="contact__item">
        <svg class="contact__icon" viewBox="0 0 16 16"><path d="M8 1 L15 8 H13 V15 H3 V8 H1 Z" fill="var(--accent)"/></svg>
        Your address goes here, 11000
      </li>
      <li class="contact__item">
        <svg class="contact__icon" viewBox="0 0 16 16"><path d="M3 1 L6 1 L7 5 L5 6.5 Q7 10 9.5 11 L11 9 L15 10 L15 13 Q14 15 11 15 Q2 12 1 4 Q1 1 3 1 Z" fill="var(--accent)"/></svg>
        000 000 0000 / 000 000 0001
      </li>
      <li class="contact__item">
        <svg class="contact__icon" viewBox="0 0 16 16"><circle cx="8" cy="8" r="6.5" fill="none" stroke="var(--accent)" stroke-width="1.5"/><ellipse cx="8" cy="8" rx="2.8" ry="6.5" fill="none" stroke="var(--accent)" stroke-width="1.2"/><line x1="1.5" y1="8" x2="14.5" y2="8" stroke="var(--accent)" stroke-width="1.2"/></svg>
        www.yourwebsite.nl
      </li>
    </ul>
  </section>
</main>
</body>
</html>
```